lab equipment website

We need a fresh new look for a company website called quorvin. We will be using the current logo and brand colors on their current website quorvin.com. They want to keep their text and on-page SEO, but would like to reformat it to look more modern and fresh. They want to have everything be high performance with a great user experience. Their main call to action is for people to fill in a contact form so they can call them. There is some information that is purposely above the fold on the instrument pages. I will need the home page, about page and a leasing page.

```html
<!DOCTYPE html>
<html lang="en">
<head>
<meta charset="utf-8">
<title>quorvin | Lab Equipment Leasing</title>
<link rel="stylesheet" href="https://fonts.googleapis.com/css2?family=Raleway:wght@400;500;600;700;800&display=swap">
<style>
  :root{
    --teal-dark:#0d5a5e;
    --teal:#0bbaa2;
    --teal-text:#17a995;
    --navy:#1d4a57;
    --footer:#27424f;
    --orange:#ff6a13;
    --white:#ffffff;
    --ink:#1a1a1a;
    --tick:#8be04e;
    --field:#ffffff;
  }
  *{box-sizing:border-box;margin:0;padding:0}
  html,body{width:1200px;height:2889px;overflow:hidden}
  body{position:relative;font-family:"Raleway",sans-serif;color:var(--ink);background:var(--white)}
  .backdrop{position:absolute;left:0;top:0;width:1200px;height:2889px;z-index:0}
  .layer{position:absolute;z-index:1}

  /* header */
  .site-header{left:0;top:0;width:1200px;height:78px;background:var(--teal-dark)}
  .brand{position:absolute;left:73px;top:18px;display:flex;align-items:center;gap:10px}
  .brand-mark{width:18px;height:18px;background:var(--teal);border-radius:3px}
  .brand-name{font-weight:800;font-size:30px;color:var(--white);letter-spacing:-.5px;line-height:1}
  .main-nav{position:absolute;left:400px;top:31px}
  .main-nav a{color:var(--white);text-decoration:none;font-weight:600;font-size:16px;position:absolute;white-space:nowrap}
  .main-nav a.active{border-bottom:2px solid var(--orange);padding-bottom:4px}

  /* hero */
  .hero-copy{left:193px;top:176px;width:240px;font-size:20px;line-height:29px;color:var(--teal-text);font-weight:500}
  .btn{display:inline-flex;align-items:center;justify-content:center;background:var(--orange);color:var(--white);font-weight:700;text-transform:uppercase;text-decoration:none;border-radius:5px}
  .hero-btn{left:193px;top:322px;width:194px;height:42px;font-size:15px}
  .hero-visual{left:453px;top:100px;width:560px;height:285px;border-radius:8px;background:linear-gradient(180deg,#f3f5f7 0%,#dfe3e8 70%,#f7f8fa 100%)}

  /* lease intro */
  .lease-title{left:0;top:497px;width:1200px;text-align:center;font-size:25px;font-weight:800;color:var(--navy);text-transform:uppercase}
  .lease-intro{left:183px;top:540px;width:840px;text-align:center;font-size:12.5px;line-height:23px;color:var(--white)}
  .plans-title{left:481px;top:680px;font-size:24px;font-weight:800;color:var(--navy);text-transform:uppercase}
  .plan-list{left:160px;top:719px;list-style:none}
  .plan-list li{display:flex;align-items:center;gap:12px;height:32.5px;font-size:12px;font-weight:800;color:var(--white);text-transform:uppercase}
  .plan-list svg{width:18px;height:14px;flex:none}
  .plans-copy{left:481px;top:719px;width:570px;font-size:15.5px;line-height:31px;color:var(--white)}
  .contact-btn{left:508px;top:953px;width:184px;height:41px;font-size:15px}

  /* equipment */
  .equip-title{left:0;top:1086px;width:1200px;text-align:center;font-size:36px;font-weight:800;color:var(--navy);text-transform:uppercase}
  .equip-grid{left:121px;top:1142px;display:grid;grid-template-columns:repeat(5,181px);column-gap:14px;grid-template-rows:283px 301px 300px 200px}
  .equip-card{display:flex;flex-direction:column;align-items:center}
  .equip-photo{width:181px;height:181px;box-shadow:0 2px 6px rgba(0,0,0,.18)}
  .equip-name{margin-top:14px;font-size:15px;font-weight:500;text-transform:uppercase;text-align:center;line-height:19px;color:var(--ink)}
  .equip-btn{margin-top:5px;width:98px;height:26px;font-size:11px;border-radius:5px}

  /* estimate form */
  .form-title{left:0;top:2377px;width:1200px;text-align:center;font-size:36px;font-weight:800;color:var(--navy);text-transform:uppercase}
  .estimate-form{left:468px;top:2452px;width:266px}
  .estimate-form input{display:block;width:266px;height:36px;margin-bottom:8.5px;border:none;border-radius:5px;background:var(--field);font-family:"Raleway",sans-serif;font-size:11px;font-weight:600;padding-left:14px;color:#9aa7ad}
  .estimate-form input::placeholder{color:#a5b1b6;text-transform:uppercase;letter-spacing:.5px}
  .send-btn{position:absolute;left:85px;top:173px;width:96px;height:27px;border:none;font-family:"Raleway",sans-serif;font-size:12px}

  /* footer */
  .footer-brand{left:135px;top:2692px;display:flex;align-items:center;gap:10px}
  .footer-brand .brand-name{font-size:30px}
  .footer-tag{left:178px;top:2725px;font-size:10px;font-weight:700;line-height:11px;color:var(--teal)}
  .footer-about{left:178px;top:2752px;width:250px;font-size:9.5px;line-height:12px;color:var(--white)}
  .connect-title{left:907px;top:2713px;font-size:21px;font-weight:500;color:var(--white)}
  .social-list{left:908px;top:2756px;display:flex;gap:8px;list-style:none}
  .social-list li{width:35px;height:35px;border-radius:50%;background:var(--orange)}
  .footer-nav{left:764px;top:2834px}
  .footer-nav a{position:absolute;color:var(--white);text-decoration:none;font-size:13px;font-weight:600;white-space:nowrap}
  .copyright{left:0;top:2864px;width:1200px;text-align:center;font-size:12px;font-weight:600;color:var(--white)}
</style>
</head>
<body>

<svg class="backdrop" viewBox="0 0 1200 2889" width="1200" height="2889" aria-hidden="true">
  <path d="M0 318 C120 330 260 470 470 462 C700 452 820 360 1000 370 C1090 375 1160 380 1200 382 L1200 1080 C1080 1070 960 1060 820 1050 C620 1036 420 1050 260 1010 C140 980 60 950 0 942 Z" fill="var(--teal)"/>
  <path d="M0 2380 C200 2375 420 2400 640 2375 C860 2350 1000 2270 1200 2266 L1200 2700 C1100 2690 1000 2640 860 2630 C680 2618 520 2640 380 2630 C220 2618 80 2600 0 2590 Z" fill="var(--teal)"/>
  <path d="M0 2590 C80 2600 220 2618 380 2630 C520 2640 680 2618 860 2630 C1000 2640 1100 2690 1200 2700 L1200 2889 L0 2889 Z" fill="var(--footer)"/>
</svg>

<header class="layer site-header">
  <div class="brand"><span class="brand-mark"></span><span class="brand-name">quorvin</span></div>
  <nav class="main-nav">
    <a href="#" style="left:0">Home</a>
    <a href="#" style="left:85px">About</a>
    <a href="#" class="active" style="left:172px">Leasing</a>
    <a href="#" style="left:270px">Contact</a>
    <a href="#" style="left:368px">FAQ</a>
  </nav>
</header>

<p class="layer hero-copy">We have a rental plan that addresses your laboratory's financial and operational needs.</p>
<a class="layer btn hero-btn" href="#">View all plans</a>
<div class="layer hero-visual" role="img" aria-label="Group of laboratory instruments: analyzer, chromatography stack and microscope"></div>

<h2 class="layer lease-title">Lease our comprehensive selection of lab equipment</h2>
<p class="layer lease-intro">So why our laboratory equipment leasing program? Because when capital is limited, purchasing equipment poses a serious burden. Fortunately there is a solution- quorvin. Our laboratory support services allow you to use equipment for a fraction of the price as well as the freedom to utilize different machines for various lengths of time, instead of being tied down to a single machine. Plus, when you collaborate with quorvin and anything goes wrong with our machine, we've got your back with our stress-free repair coverage. With quorvin's all-inclusive equipment packages, there is an affordable solution to an expensive problem.</p>

<h3 class="layer plans-title">All plans include</h3>
<ul class="layer plan-list">
  <li><svg viewBox="0 0 18 14"><path d="M1 7 L6.5 12 L17 1.5" fill="none" stroke="var(--tick)" stroke-width="2.5"/></svg>Equipment preventive maintenance</li>
  <li><svg viewBox="0 0 18 14"><path d="M1 7 L6.5 12 L17 1.5" fill="none" stroke="var(--tick)" stroke-width="2.5"/></svg>Machine repair coverage</li>
  <li><svg viewBox="0 0 18 14"><path d="M1 7 L6.5 12 L17 1.5" fill="none" stroke="var(--tick)" stroke-width="2.5"/></svg>Flexible payment schedules</li>
  <li><svg viewBox="0 0 18 14"><path d="M1 7 L6.5 12 L17 1.5" fill="none" stroke="var(--tick)" stroke-width="2.5"/></svg>Email &amp; phone customer support</li>
  <li><svg viewBox="0 0 18 14"><path d="M1 7 L6.5 12 L17 1.5" fill="none" stroke="var(--tick)" stroke-width="2.5"/></svg>Quick delivery &amp; installation</li>
  <li><svg viewBox="0 0 18 14"><path d="M1 7 L6.5 12 L17 1.5" fill="none" stroke="var(--tick)" stroke-width="2.5"/></svg>Technical training</li>
  <li><svg viewBox="0 0 18 14"><path d="M1 7 L6.5 12 L17 1.5" fill="none" stroke="var(--tick)" stroke-width="2.5"/></svg>Substantial tax deductions*</li>
</ul>
<p class="layer plans-copy">Whether you need the newest equipment or more affordable refurbished options, we have a laboratory equipment leasing package that addresses your business' financial and operational needs. If you don't see an instrument that you're interested in below, not to worry. We can source virtually any equipment-type. Contact us and we'll create a custom solution just for you.</p>
<a class="layer btn contact-btn" href="#">Contact us</a>

<h2 class="layer equip-title">Popular equipment</h2>
<div class="layer equip-grid">
  <div class="equip-card"><div class="equip-photo" role="img" aria-label="Autoclave" style="background:linear-gradient(#f2f2f2,#8a8f94)"></div><p class="equip-name">Autoclaves</p><a class="btn equip-btn" href="#">View</a></div>
  <div class="equip-card"><div class="equip-photo" role="img" aria-label="Lab balance" style="background:linear-gradient(#f7f7f7,#cfd3d6)"></div><p class="equip-name">Lab balances</p><a class="btn equip-btn" href="#">View</a></div>
  <div class="equip-card"><div class="equip-photo" role="img" aria-label="Centrifuge" style="background:linear-gradient(#f6f6f6,#d8d9da)"></div><p class="equip-name">Centrifuges</p><a class="btn equip-btn" href="#">View</a></div>
  <div class="equip-card"><div class="equip-photo" role="img" aria-label="Microscope" style="background:linear-gradient(#f5f5f5,#b5b8bb)"></div><p class="equip-name">Microscopes</p><a class="btn equip-btn" href="#">View</a></div>
  <div class="equip-card"><div class="equip-photo" role="img" aria-label="Cryostat" style="background:linear-gradient(#f7f7f7,#d4d6d8)"></div><p class="equip-name">Cryostats</p><a class="btn equip-btn" href="#">View</a></div>

  <div class="equip-card"><div class="equip-photo" role="img" aria-label="DNA double helix for sequencers" style="background:linear-gradient(135deg,#06253f,#2b7fb5)"></div><p class="equip-name">Next generation<br>sequencers</p><a class="btn equip-btn" href="#">View</a></div>
  <div class="equip-card"><div class="equip-photo" role="img" aria-label="Gloved hand holding a sample tube" style="background:linear-gradient(135deg,#e9eef3,#8fb0d6)"></div><p class="equip-name">Flow cytometers</p><a class="btn equip-btn" href="#">View</a></div>
  <div class="equip-card"><div class="equip-photo" role="img" aria-label="Gloved hand loading a PCR plate" style="background:linear-gradient(135deg,#c9d9ee,#3b6fc2)"></div><p class="equip-name">PCR systems</p><a class="btn equip-btn" href="#">View</a></div>
  <div class="equip-card"><div class="equip-photo" role="img" aria-label="Multichannel pipette dispensing liquid" style="background:linear-gradient(135deg,#0a2c55,#3aa6e6)"></div><p class="equip-name">Liquid handlers</p><a class="btn equip-btn" href="#">View</a></div>
  <div class="equip-card"><div class="equip-photo" role="img" aria-label="Microplate close-up" style="background:linear-gradient(135deg,#7fc0c9,#8b6b5a)"></div><p class="equip-name">Microplate readers</p><a class="btn equip-btn" href="#">View</a></div>

  <div class="equip-card"><div class="equip-photo" role="img" aria-label="Sample tubes in an analyzer" style="background:linear-gradient(135deg,#0e2a48,#5aa0d8)"></div><p class="equip-name">Clinical chemistry<br>analyzers</p><a class="btn equip-btn" href="#">View</a></div>
  <div class="equip-card"><div class="equip-photo" role="img" aria-label="Rack of blood sample tubes" style="background:linear-gradient(180deg,#8a1f22,#dfe4e6)"></div><p class="equip-name">Blood bank<br>analyzers</p><a class="btn equip-btn" href="#">View</a></div>
  <div class="equip-card"><div class="equip-photo" role="img" aria-label="Protein ribbon model" style="background:linear-gradient(135deg,#f2f6f3,#5aa65a 55%,#3a6fd0)"></div><p class="equip-name">Peptide<br>synthesizers</p><a class="btn equip-btn" href="#">View</a></div>
  <div class="equip-card"><div class="equip-photo" role="img" aria-label="Microarray dot grid" style="background:linear-gradient(135deg,#0b0b0b,#2e3a12)"></div><p class="equip-name">Microarray<br>scanners</p><a class="btn equip-btn" href="#">View</a></div>
  <div class="equip-card"><div class="equip-photo" role="img" aria-label="Spectrophotometer" style="background:linear-gradient(135deg,#f5f5f5,#a9b0b4)"></div><p class="equip-name">Spectrophoto-<br>meters</p><a class="btn equip-btn" href="#">View</a></div>

  <div class="equip-card"><div class="equip-photo" role="img" aria-label="Blue stained gel bands" style="background:linear-gradient(135deg,#dfe8f5,#3d63c4)"></div><p class="equip-name">Western blot<br>imaging systems</p><a class="btn equip-btn" href="#">View</a></div>
  <div class="equip-card"><div class="equip-photo" role="img" aria-label="Infrared spectrometer" style="background:linear-gradient(135deg,#9aa7b3,#2c4a78)"></div><p class="equip-name">Infrared<br>spectrometers</p><a class="btn equip-btn" href="#">View</a></div>
  <div class="equip-card"><div class="equip-photo" role="img" aria-label="Amber resin beads" style="background:linear-gradient(135deg,#f0a22a,#9a4f08)"></div><p class="equip-name">Ion<br>chromatography</p><a class="btn equip-btn" href="#">View</a></div>
  <div class="equip-card"><div class="equip-photo" role="img" aria-label="Gas chromatography instruments" style="background:linear-gradient(135deg,#f4f4f4,#b9bdc1)"></div><p class="equip-name">Gas<br>chromatography</p><a class="btn equip-btn" href="#">View</a></div>
  <div class="equip-card"><div class="equip-photo" role="img" aria-label="Mass spectrometer in a lab" style="background:linear-gradient(135deg,#cfe0ea,#5d8198)"></div><p class="equip-name">Mass<br>spectrometers</p><a class="btn equip-btn" href="#">View</a></div>
</div>

<h2 class="layer form-title">Request a lease estimate</h2>
<form class="layer estimate-form">
  <input type="text" placeholder="Full name">
  <input type="email" placeholder="Email address">
  <input type="tel" placeholder="Phone number">
  <input type="text" placeholder="Instrument type">
  <button class="btn send-btn" type="submit">Send</button>
</form>

<div class="layer footer-brand"><span class="brand-mark"></span><span class="brand-name">quorvin</span></div>
<p class="layer footer-tag">your success,<br>our support.</p>
<p class="layer footer-about">We are a team of Halden University scientists driven by our passion for research. We strive to serve the scientific community. We love what we do, and who we work with. Together we can make positive changes in the world of research.</p>

<p class="layer connect-title">Connect With Us</p>
<ul class="layer social-list" aria-label="Social links">
  <li></li><li></li><li></li><li></li>
</ul>

<nav class="layer footer-nav">
  <a href="#" style="left:0">Home</a>
  <a href="#" style="left:66px">About</a>
  <a href="#" style="left:136px">Leasing</a>
  <a href="#" style="left:214px">Contact</a>
  <a href="#" style="left:292px">FAQ</a>
</nav>
<p class="layer copyright">quorvin © | 2018 | All Rights Reserved.</p>

</body>
</html>
```